Harbour Blokes - community/social/support group for men needs a flyer

We need a flyer for our community group for display in GP clinics and other community services offices. Please refer to our website for design ideas: www.harbourblokes.org.au. We need it to be clean and simple to read.

Target Market(s)

Men 18+

Font styles to use
Serif

Colors
00a990

```html
<!DOCTYPE html>
<html lang="en">
<head>
<meta charset="utf-8">
<title>Harbour Blokes – Flyer</title>
<link href="https://fonts.googleapis.com/css2?family=Montserrat:ital,wght@0,300;0,400;0,600;0,700;0,800;1,400&display=swap" rel="stylesheet">
<style>
  :root {
    --teal: #00a990;
    --teal-bright: #16ad95;
    --teal-mid: #168a74;
    --forest: #17604f;
    --forest-deep: #137a67;
    --panel-grey: #d4d5d7;
    --ink: #1a1a1a;
    --white: #ffffff;
  }
  * { margin: 0; padding: 0; box-sizing: border-box; }
  html, body { width: 848px; height: 1200px; overflow: hidden; background: var(--white); }
  body { font-family: "Montserrat", sans-serif; color: var(--ink); }

  .flyer { position: relative; width: 848px; height: 1200px; overflow: hidden; }
  .backdrop { position: absolute; inset: 0; width: 848px; height: 1200px; }

  .headline {
    position: absolute; left: 38px; top: 384px;
    color: var(--white); font-weight: 800; font-size: 41px; line-height: 59.4px;
    letter-spacing: 0.3px;
  }

  .brand { position: absolute; left: 420px; top: 607px; width: 366px; text-align: center; }
  .brand-name {
    font-weight: 600; font-size: 34px; letter-spacing: 1.5px; color: var(--ink); line-height: 46px;
    white-space: nowrap;
  }
  .brand-tagline {
    margin-top: 2px; font-size: 15px; color: var(--teal); white-space: nowrap;
    display: flex; justify-content: space-between; padding: 0 4px;
  }
  .brand-tagline .dot { color: var(--ink); }

  .about {
    position: absolute; left: 55px; top: 729px; width: 328px;
    font-weight: 300; font-size: 17px; line-height: 23px; text-align: justify;
    color: var(--ink);
  }

  .projects { position: absolute; left: 432px; top: 698px; width: 360px; }
  .projects-intro { font-style: italic; font-size: 17px; line-height: 22px; }
  .projects-list { list-style: none; margin-top: 16px; }
  .projects-list li { font-weight: 600; font-size: 19px; line-height: 34.2px; white-space: nowrap; }
  .projects-list li::before { content: "•"; margin-right: 6px; font-size: 14px; vertical-align: 2px; }
  .projects-list .note { font-weight: 400; font-style: italic; font-size: 15px; }
  .projects-more { font-style: italic; font-size: 17px; margin-left: 10px; margin-top: -2px; }

  .get-involved {
    position: absolute; right: 24px; top: 1014px; text-align: right;
    color: var(--white); font-size: 15px; line-height: 21px; font-weight: 400;
  }
  .get-involved .web { font-weight: 700; font-size: 18.5px; margin-top: 6px; line-height: 24px; }

  .social {
    position: absolute; right: 24px; top: 1144px; text-align: right; color: var(--white);
  }
  .social p { font-size: 14.5px; line-height: 20px; }
  .social .handle { font-weight: 700; font-size: 16.5px; line-height: 26px; }
</style>
</head>
<body>
<div class="flyer">
  <svg class="backdrop" viewBox="0 0 1500 2122" preserveAspectRatio="none">
    <defs>
      <linearGradient id="photoTone" x1="0" y1="0" x2="1" y2="1">
        <stop offset="0" stop-color="#5d7f45"/>
        <stop offset="0.35" stop-color="#9a8a6e"/>
        <stop offset="0.6" stop-color="#c98a7a"/>
        <stop offset="1" stop-color="#8a5a55"/>
      </linearGradient>
    </defs>
    <rect class="photo" x="0" y="0" width="1500" height="1100" fill="url(#photoTone)" role="img" aria-label="Photo of three smiling men with arms around each other outdoors among green trees"/>
    <polygon class="band-forest" points="0,625 130,570 900,880 0,1170" fill="var(--forest)" opacity="0.92"/>
    <polygon class="band-mid" points="0,1170 900,880 1070,815 0,1210" fill="var(--teal-mid)"/>
    <polygon class="band-teal" points="0,1205 1070,815 1500,985 1500,1025 1070,850 0,1285" fill="var(--teal-bright)"/>
    <polygon class="sheet" points="0,1285 1070,850 1500,1025 1500,2122 0,2122" fill="var(--white)"/>
    <rect class="projects-panel" x="728" y="1218" width="682" height="860" rx="30" fill="var(--panel-grey)"/>
    <polygon class="corner-teal" points="576,2010 1500,1635 1500,2010" fill="var(--teal-bright)"/>
    <polygon class="footer-band" points="300,2122 576,2010 1500,2010 1500,2122" fill="var(--forest-deep)"/>
  </svg>

  <h1 class="headline">Social<br>Support<br>Mateship<br>Community</h1>

  <div class="brand">
    <div class="brand-name">HARBOUR BLOKES</div>
    <div class="brand-tagline">
      <span>Social</span><span class="dot">•</span><span>Support</span><span class="dot">•</span><span>Mateship</span><span class="dot">•</span><span>Community</span>
    </div>
  </div>

  <p class="about">Harbour Blokes Inc. is a community group that supports the positive activity, engagement and inclusion of men in Port Wallaby’s Eastern Foreshore. Our aim is to reduce the number of men who are socially disadvantaged, marginalised or isolated to become productive, active members of the local community. We do this by providing opportunities for men (18 years+) to come together in open, non-judgemental, safe spaces and participate in a range of social activities that encourage new friendships, normalise help-seeking behaviours and link with local support services.</p>

  <section class="projects">
    <p class="projects-intro">We run a number of projects each year,<br>which currently include:</p>
    <ul class="projects-list">
      <li>Dads &amp; kids playgroup</li>
      <li>Games Night</li>
      <li>Yarning Circle <span class="note">(Men’s discussion group)</span></li>
      <li>GBTIQ + Social Dinners</li>
      <li>Shared Services working bee’s</li>
      <li>Guest speakers</li>
      <li>Annual men’s gathering</li>
    </ul>
    <p class="projects-more">and more...</p>
  </section>

  <div class="get-involved">
    <p>For a list of<br>our current activities and to<br>find out how you can get involved,<br>please visit us online at :</p>
    <p class="web">www.harbourblokes.org.au</p>
  </div>

  <div class="social">
    <p>Join our Chatterbook page for our latest updates :</p>
    <p class="handle">www.chatterbook.com/harbourblokesAU/</p>
  </div>
</div>
</body>
</html>
```